Splash screen for website with map to choose location

Hello,

We have a website http://new.brivonlux.com. We need to do a splash page when the user first arrives with a map. The company is an LED technology company. The closest we can find to something we like is http://global.perizo/en/support/ where you select your region but we need something that fits our website and is unique to technology/LED/lighting.

Thank you!
Dorwin

Target Market(s)

Buyers of LED lights who are contractors for hotels, restaurants, etc.

Industry/Entity Type

It Company

Number of Pages Required

1 page

Font styles to use
Sans Serif

Colors
0592cd

Requirements
Must have
• It must have the same header and footer as http://new.brivonlux.com. It must be a map like the Perizo page http://global.perizo/en/support/ but different/unique to the LED or lighting industry and fit in with the overall website feel.
• NOTE: This site is forcing me to choose colors and fonts but I want you to use the same as our current website http://new.brivonlux.com.
• If you have any questions feel free to ask! I hope to find a great design and work with you for more projects in the future!

```html
<!DOCTYPE html>
<html lang="en">
<head>
<meta charset="utf-8">
<title>Brivonlux – Select Region</title>
<link href="https://fonts.googleapis.com/css2?family=Catamaran:wght@300;400;700&display=swap" rel="stylesheet">
<style>
:root{
  --brand:#0592cd;
  --ink:#222;
  --text:#333;
  --muted:#555;
  --topbar:#f4f4f4;
  --page:#efefef;
  --panel:#fff;
  --tile:#f7f7f7;
  --map:#777;
  --social:#cfcfcf;
}
*{box-sizing:border-box;margin:0;padding:0}
html,body{width:1058px;height:1200px;overflow:hidden}
body{position:relative;background:var(--page);font-family:"Catamaran",Arial,sans-serif;color:var(--text)}
.abs{position:absolute}
.topbar{left:0;top:0;width:1058px;height:34px;background:var(--topbar)}
.topbar .util{top:9px;font-size:13px;color:var(--ink);letter-spacing:.3px}
.social{display:flex;gap:6px}
.social span{width:20px;height:20px;border-radius:50%;background:var(--social);display:block}
.search{left:711px;top:6px;width:237px;height:22px;background:#fff}
.search .btn{right:0;top:0;width:29px;height:22px;background:#c4c4c4}
.header{left:0;top:34px;width:1058px;height:84px;background:#fff}
.brand-name{font-weight:400;letter-spacing:11px;color:#333;text-transform:lowercase}
.brand-dot{border-radius:50%;background:var(--brand)}
.tagline{color:var(--brand);font-size:10.5px;letter-spacing:.2px}
.nav{top:24px;left:350px;display:flex;gap:15px;font-size:13.5px;color:var(--ink);letter-spacing:.2px}
.rule{left:102px;width:855px;height:1px;background:var(--brand)}
.hero-bg{left:0;top:118px;width:1058px;height:675px;background:radial-gradient(ellipse at 50% 45%,#e6e3df 0%,#ececec 45%,#efefef 80%)}
.title{left:0;width:1058px;top:190px;text-align:center;font-size:33px;font-weight:300;color:var(--ink)}
.tile{top:262px;width:127px;height:127px;background:var(--tile)}
.tile.active{background:var(--brand)}
.tile .map{position:absolute;left:24px;top:28px;width:79px;height:70px;border-radius:40%;background:var(--map)}
.tile.active .map{background:#fff}
.region{top:404px;width:145px;text-align:center;font-size:16px;color:var(--ink)}
.panel{left:102px;top:454px;width:855px;height:254px;background:var(--panel)}
.pointer{left:161px;top:446px;width:0;height:0;border-left:8px solid transparent;border-right:8px solid transparent;border-bottom:8px solid var(--panel)}
.countries{font-family:Arial,Helvetica,sans-serif;font-size:11px;color:#222}
.countries li{list-style:none;height:26.4px;display:flex;align-items:center}
.flag{width:15px;height:10px;margin-right:12px;flex:none}
.footer-rule{top:793px}
.f-head{font-weight:700;font-size:11px;color:#111;letter-spacing:.2px}
.f-text{font-size:11px;line-height:14.5px;color:var(--text)}
.f-text em{font-style:italic}
.links{font-size:11px;line-height:19px;color:var(--text);text-transform:uppercase;padding-left:3px;border-left:1px solid #ccc}
.links b{color:#111}
.vsocial{left:927px;top:879px;display:flex;flex-direction:column;gap:6px}
.vsocial span{width:20px;height:20px;border-radius:50%;background:var(--social);display:block}
</style>
</head>
<body>

<div class="abs topbar">
  <div class="abs util" style="left:110px">EN ▾</div>
  <div class="abs util" style="left:160px">SUPPORT</div>
  <div class="abs util" style="left:239px">REP LOGIN</div>
  <div class="abs social" style="left:595px;top:7px"><span></span><span></span><span></span><span></span></div>
  <div class="abs search"><div class="abs btn">
    <svg width="29" height="22" viewBox="0 0 29 22"><circle cx="13.5" cy="10" r="4.5" fill="none" stroke="#fff" stroke-width="1.6"/><line x1="16.8" y1="13.3" x2="20" y2="16.5" stroke="#fff" stroke-width="1.8"/></svg>
  </div></div>
</div>

<header class="abs header">
  <div class="abs brand-dot" style="left:110px;top:20px;width:16px;height:16px"></div>
  <div class="abs brand-name" style="left:134px;top:16px;font-size:19px">Brivonlux</div>
  <div class="abs tagline" style="left:110px;top:54px">Complete Integrated LED Lighting Solutions</div>
  <nav class="abs nav"><span>HOME</span><span>ABOUT US</span><span>PRODUCTS</span><span>APPLICATIONS</span><span>PROJECTS</span><span>NEWS</span><span>AGENT FINDER</span><span>CONTACT</span></nav>
</header>
<div class="abs rule" style="top:118px"></div>

<div class="abs hero-bg" role="img" aria-label="Soft, faded photograph of glowing LED light bulbs"></div>

<div class="abs brand-dot" style="left:518px;top:162px;width:20px;height:20px"></div>
<h1 class="abs title">Select Region</h1>

<div class="abs tile active" style="left:105px"><div class="map" role="img" aria-label="Map of Europe"></div></div>
<div class="abs tile" style="left:250px"><div class="map" role="img" aria-label="Map of Africa"></div></div>
<div class="abs tile" style="left:394px"><div class="map" role="img" aria-label="Map of North America"></div></div>
<div class="abs tile" style="left:540px"><div class="map" role="img" aria-label="Map of South America"></div></div>
<div class="abs tile" style="left:684px"><div class="map" role="img" aria-label="Map of Asia"></div></div>
<div class="abs tile" style="left:827px"><div class="map" role="img" aria-label="Map of Oceania"></div></div>

<div class="abs region" style="left:96px">Europe</div>
<div class="abs region" style="left:241px">Africa</div>
<div class="abs region" style="left:385px">North America</div>
<div class="abs region" style="left:532px">South America</div>
<div class="abs region" style="left:675px">Asia</div>
<div class="abs region" style="left:816px">Oceania</div>

<div class="abs pointer"></div>
<div class="abs panel"></div>

<ul class="abs countries" style="left:124px;top:474px">
  <li><span class="flag" style="background:#d7262b"></span>Armenia</li>
  <li><span class="flag" style="background:#e0373e"></span>Austria</li>
  <li><span class="flag" style="background:#c8313e"></span>Belarus</li>
  <li><span class="flag" style="background:#e8c320"></span>Belgium</li>
  <li><span class="flag" style="background:#1e3f96"></span>Bosnia &amp; Herzegovina</li>
  <li><span class="flag" style="background:#3a9a4f"></span>Bulgaria</li>
  <li><span class="flag" style="background:#2a5aa8"></span>Czech Republic</li>
  <li><span class="flag" style="background:#d52b3a"></span>Denmark</li>
</ul>
<ul class="abs countries" style="left:272px;top:474px">
  <li><span class="flag" style="background:#1d5fac"></span>Estonia</li>
  <li><span class="flag" style="background:#2b63b8"></span>Faroe Islands</li>
  <li><span class="flag" style="background:#2e5fa8"></span>Finland</li>
  <li><span class="flag" style="background:#3a5fb0"></span>France</li>
  <li><span class="flag" style="background:#d6342b"></span>Germany</li>
  <li><span class="flag" style="background:#dc3a3a"></span>Gibraltar</li>
  <li><span class="flag" style="background:#3d74c4"></span>Greece</li>
  <li><span class="flag" style="background:#f0d24a"></span>Vatican City State</li>
</ul>
<ul class="abs countries" style="left:422px;top:474px">
  <li><span class="flag" style="background:#3a9a4f"></span>Hungary</li>
  <li><span class="flag" style="background:#2b5aa6"></span>Iceland</li>
  <li><span class="flag" style="background:#3aa05a"></span>Ireland</li>
  <li><span class="flag" style="background:transparent"></span>Isle Of Man</li>
  <li><span class="flag" style="background:#3aa05a"></span>Italy</li>
  <li><span class="flag" style="background:#9e3039"></span>Latvia</li>
  <li><span class="flag" style="background:#2b4fa8"></span>Liechtenstein</li>
  <li><span class="flag" style="background:#f0c330"></span>Lithuania</li>
</ul>
<ul class="abs countries" style="left:561px;top:474px">
  <li><span class="flag" style="background:#e05050"></span>Luxembourg</li>
  <li><span class="flag" style="background:#e8732a"></span>Macedonia</li>
  <li><span class="flag" style="background:#d8363a"></span>Malta</li>
  <li><span class="flag" style="background:#d8363a"></span>Monaco</li>
  <li><span class="flag" style="background:#d8363a"></span>Montenegro</li>
  <li><span class="flag" style="background:#c8313e"></span>Netherlands</li>
  <li><span class="flag" style="background:#d8363a"></span>Norway</li>
  <li><span class="flag" style="background:#d8363a"></span>Poland</li>
</ul>
<ul class="abs countries" style="left:693px;top:474px">
  <li><span class="flag" style="background:#c8312b"></span>Portugal</li>
  <li><span class="flag" style="background:#f0c330"></span>Romania</li>
  <li><span class="flag" style="background:#2b5aa6"></span>Russian Federation</li>
  <li><span class="flag" style="background:#c8313e"></span>Serbia</li>
  <li><span class="flag" style="background:#2b5aa6"></span>Slovakia</li>
  <li><span class="flag" style="background:#2b5aa6"></span>Slovenia</li>
  <li><span class="flag" style="background:#e8b020"></span>Spain</li>
  <li><span class="flag" style="background:#2b66a8"></span>Sweden</li>
</ul>
<ul class="abs countries" style="left:837px;top:474px">
  <li><span class="flag" style="background:#d8262b"></span>Switzerland</li>
  <li><span class="flag" style="background:#d8262b"></span>Turkey</li>
  <li><span class="flag" style="background:#f0d030"></span>Ukraine</li>
  <li><span class="flag" style="background:#2b3f86"></span>United Kingdom</li>
</ul>

<div class="abs rule footer-rule"></div>

<div class="abs brand-dot" style="left:110px;top:818px;width:13px;height:13px"></div>
<div class="abs brand-name" style="left:142px;top:815px;font-size:15px;letter-spacing:9px">Brivonlux</div>
<div class="abs tagline" style="left:110px;top:842px;font-size:8.5px">Complete Integrated LED Lighting Solutions</div>

<div class="abs" style="left:110px;top:878px;width:150px">
  <div class="f-head">NY HEADQUARTERS</div>
  <div class="f-text">418 W 27th St, Suite 9C<br>New York, NY 10001<br><em>info@brivonlux.com</em></div>
  <div class="f-head" style="margin-top:11px">SHENZHEN OFFICE</div>
  <div class="f-text">7/F Block C, Hengtai Industrial Park, Xixiang 3rd Road, Bao'An Shenzhen, China, 518102<br>深圳市宝安区西乡三路恒泰工业园C座7楼 518102<br><em>saleschina@brivonlux.com</em></div>
  <div class="f-head" style="margin-top:11px">DUBAI OFFICE</div>
  <div class="f-text">* Address Coming Soon<br><em>salesme@brivonlux.com</em></div>
</div>

<div class="abs" style="left:274px;top:878px;width:190px">
  <div class="f-head">NJ PRODUCTION FACILITY</div>
  <div class="f-text">62 Orchard St, Garfield, NJ 07026</div>
  <div class="f-head" style="margin-top:40px">HONG KONG OFFICE</div>
  <div class="f-text">Unit 22, 5/F, Kin Wah Ind. Building 8-10 Hoi Yuen Rd. Kwun Tong, Hong Kong<br><em>saleshk@brivonlux.com</em></div>
  <div class="f-head" style="margin-top:55px">SYDNEY OFFICE</div>
  <div class="f-text">U12. 4-20 Marlow street, Kallangur Queensland, P.O. BOX 88, Australia 4503<br><em>salesanz@brivonlux.com</em></div>
</div>

<div class="abs links" style="left:508px;top:879px;height:202px">About us<br>Agent finder<br>Contact us<br>Applications<br>News<br>Support<br>Careers<br>Privacy<br>Terms &amp; conditions<br>Sitemap</div>
<div class="abs links" style="left:655px;top:879px;height:202px"><b>Products</b><br>Ribbonlux<br>Channels<br>Panel Lux | Backlux<br>Rigid AC<br>Linearlux fixtures<br>Events &amp; entertainment<br>Spots &amp; floods<br>High power linear<br>High bay</div>
<div class="abs links" style="left:802px;top:879px;height:220px"><b>Projects</b><br>Arts &amp; education<br>Healthcare<br>Hotels<br>Restaurants<br>Retail<br>Sports and leisure<br>Structures<br>Transport<br>Urban<br>Workplaces</div>

<div class="abs vsocial"><span></span><span></span><span></span><span></span></div>

</body>
</html>
```